Business Card Design

I'm a authorized Glidera dealer that specilaizes in Rentals, Tours, Sales and Service of Glideras. Tours of the ocean coach, rides on the white sand.
Updates

Hi i'm sorry apparently i was using IE is why the logos weren't uploaded. I have now uploaded the logos. The pier is to be on back of card, the logo on front anf if there is a a way to make room for the actual Glideras somewhere that would be great. Thank You

Target Market(s)

tourists, 25-55 age group, income level 50,000.00 per year

Industry/Entity Type

Business

Contact Information for Business Card

Tide Row Glidera
714-555-0186
www.tiderowglidera.example
tiderowglidera@mailbox.example
"Ride the Shoreline" maybe have this
862 Larkin Ave Suite 204C
Huntington Beach, CA 92648
Only authorized Glidera dealer in the Huntington Beach area

Requirements
Nice to have
• just something that attracts fun

```html
<!DOCTYPE html>
<html lang="en">
<head>
<meta charset="utf-8">
<title>Tide Row Glidera — Business Card</title>
<link rel="stylesheet" href="https://fonts.googleapis.com/css2?family=Quicksand:wght@400;500;600&display=swap">
<style>
  :root {
    --sky-top: #3f95cf;
    --sky-low: #9fd0ea;
    --sea-deep: #1c8fb8;
    --sea-light: #4fd0d4;
    --shore: #bfe4e0;
    --sand: #efe8dc;
    --sand-shadow: #c9b9a2;
    --wood: #b98a5a;
    --navy: #123e66;
    --icon-blue: #1d5c8f;
    --white: #ffffff;
  }
  * { margin: 0; padding: 0; box-sizing: border-box; }
  html, body { width: 1200px; height: 702px; overflow: hidden; background: #ffffff; }
  .card {
    position: relative;
    width: 1200px;
    height: 702px;
    overflow: hidden;
    font-family: "Quicksand", sans-serif;
    color: var(--white);
  }
  .beach-scene {
    position: absolute;
    inset: 0;
    background:
      radial-gradient(ellipse 380px 170px at 880px 620px, rgba(185,138,90,0.55), rgba(185,138,90,0) 70%),
      radial-gradient(ellipse 360px 170px at 300px 620px, rgba(185,138,90,0.55), rgba(185,138,90,0) 70%),
      linear-gradient(180deg,
        var(--sky-top) 0px,
        var(--sky-low) 268px,
        var(--sea-deep) 272px,
        var(--sea-light) 380px,
        var(--shore) 468px,
        var(--sand) 490px,
        var(--sand-shadow) 702px);
  }
  .brand {
    position: absolute;
    left: 144px;
    top: 112px;
    width: 460px;
    font-weight: 600;
    font-size: 64px;
    line-height: 1.05;
    color: var(--navy);
  }
  .contact-list {
    position: absolute;
    left: 63px;
    top: 311px;
    list-style: none;
  }
  .contact-item {
    display: flex;
    align-items: center;
    height: 62px;
    font-size: 40px;
    font-weight: 400;
    white-space: nowrap;
  }
  .contact-item.email { font-size: 34px; }
  .contact-icon {
    flex: none;
    width: 44px;
    height: 44px;
    border-radius: 50%;
    background: radial-gradient(circle at 40% 35%, #4f8fc4, var(--icon-blue) 60%, #0d3157);
    border: 2px solid var(--white);
    display: flex;
    align-items: center;
    justify-content: center;
    font-size: 30px;
    line-height: 1;
    margin-right: 12px;
    padding-bottom: 4px;
  }
  .address {
    position: absolute;
    left: 770px;
    top: 343px;
    width: 400px;
    text-align: center;
    font-size: 22px;
    line-height: 36px;
    font-style: normal;
  }
  .tagline {
    position: absolute;
    left: 664px;
    top: 550px;
    width: 380px;
    text-align: center;
    font-weight: 500;
    font-size: 34px;
    line-height: 44px;
  }
  .website {
    position: absolute;
    left: 660px;
    top: 612px;
    width: 460px;
    text-align: center;
    font-size: 30px;
    line-height: 40px;
    white-space: nowrap;
  }
</style>
</head>
<body>
  <div class="card">
    <div class="beach-scene" role="img" aria-label="Photograph of a sunny beach: blue sky, turquoise ocean, white sand, a white umbrella on a wooden pole and two wooden lounge chairs"></div>

    <div class="brand">Tide Row Glidera</div>

    <ul class="contact-list">
      <li class="contact-item phone"><span class="contact-icon">p</span>714.555.0186</li>
      <li class="contact-item email"><span class="contact-icon">e</span>tiderowglidera@mailbox.example</li>
    </ul>

    <address class="address">
      862 Larkin Ave, Suite 204C<br>
      Huntington Beach, CA 92648
    </address>

    <div class="tagline">Ride the Shoreline</div>
    <div class="website">www.tiderowglidera.example</div>
  </div>
</body>
</html>
```